Brightvale Inc. Business Card Design

Brightvale Inc. is in search of a great clean design for our business cards!

Looking to incorporate our full logo and watermark on side one (however, I am open to having the text and watermark separated within the design.)

On side two, I am looking to have contact information (Name, Position, Phone #, Email, Website (www.thebrightvale.ca). Can have the logo and/or watermark as part of the design if applicable.

Please add tagline "Where Shine Counts" on either side 1 or 2. This tagline can be in a sans serif, serif or cursive font as long as it compliments overall design. Capitalization can be title or sentence case depending on how it fits within the design.

Get creative!! Looking for a clean, crisp, premium design! Looking for a glossy card finish with spot UV features when printed. Cards will also be printed with rounded corners. Standard dimensions (3.5 x 2).

Target Market(s)

B2B - primary clients are business owners or property management corporations. (residential jobs are few and far between)

Industry/Entity Type

Business

Contact Information for Business Card

- clean, crisp design
- double sided
- spot UV accents and glossy finish upon printing
- standard business card size (3.5 x 2) with rounded corners
- please see project description for requirements per side

Font styles to use
Sans Serif

Requirements
Must have
• - adequate bleeds with print ready files
• - cohesive design elements between side 1 & 2
• - spot UV elements (can be on both sides or just one, use your discretion)
• - colour pallet should match the logo file provided
• - incorporate tagline "where shine counts" (this tagline can be in a serif or sans serif font as long as it is complimentary to the overall design.
Nice to have
• - Premium elements with a clean design
Should not have
• - Please omit cartoon or whimsical like designs, think premium.
• - Colours should not stray from the pallet of the provided logo.

```html
<!DOCTYPE html>
<html lang="en">
<head>
<meta charset="utf-8">
<title>Brightvale Inc. Business Card</title>
<link rel="stylesheet" href="https://fonts.googleapis.com/css2?family=Montserrat:wght@700;800&family=Roboto:wght@300;400;500&display=swap">
<style>
  :root {
    --teal: #00b9bf;
    --navy: #1c2657;
    --navy-dark: #11183a;
    --white: #ffffff;
    --ink: #1d1d1d;
    --stage: #2a2a2a;
  }
  * { box-sizing: border-box; margin: 0; padding: 0; }
  html, body {
    width: 1200px; height: 900px; overflow: hidden;
    background: var(--stage);
    font-family: "Roboto", Arial, sans-serif;
  }
  .card {
    position: absolute; left: 250px;
    width: 700px; height: 400px;
    border-radius: 26px; overflow: hidden;
    box-shadow: 0 10px 30px rgba(0,0,0,.5);
  }
  .card--front { top: 30px; background: var(--teal); }
  .card--back { top: 470px; background: var(--white); }

  .brand { display: flex; align-items: center; gap: 14px; }
  .brand__mark { flex: none; }
  .brand__name {
    font-family: "Montserrat", Arial, sans-serif; font-weight: 800;
    letter-spacing: -0.5px; line-height: 1;
  }
  .card--front .brand {
    position: absolute; left: 0; right: 0; top: 140px; justify-content: center;
  }
  .card--front .brand__mark { width: 58px; height: 58px; background: var(--navy); }
  .card--front .brand__name { color: var(--white); font-size: 56px; }
  .tagline {
    font-family: "Montserrat", Arial, sans-serif; font-weight: 700;
    text-transform: uppercase; letter-spacing: 1.5px;
  }
  .card--front .tagline {
    position: absolute; left: 0; right: 0; top: 214px; text-align: center;
    color: var(--navy); font-size: 15px;
  }
  .card--front .web {
    position: absolute; left: 0; right: 0; bottom: 40px; text-align: center;
    color: var(--white); font-size: 17px; font-weight: 400;
  }

  .panel {
    position: absolute; inset: 0; background: var(--teal);
    clip-path: polygon(48% 0, 100% 0, 100% 100%, 62% 100%);
    filter: drop-shadow(-4px 0 6px rgba(0,0,0,.25));
  }
  .ribbon {
    position: absolute; left: 300px; top: 40px; width: 360px; height: 70px;
    background: var(--navy);
    clip-path: polygon(0 0, 100% 0, 88% 100%, 0 100%);
    color: var(--white); text-align: center; padding: 14px 50px 0 0;
  }
  .ribbon__fold {
    position: absolute; left: 300px; top: 110px; width: 0; height: 0;
    border-top: 22px solid var(--navy-dark); border-left: 36px solid transparent;
  }
  .ribbon__name { font-size: 24px; font-weight: 300; letter-spacing: .5px; }
  .ribbon__role { font-size: 13px; font-weight: 400; margin-top: 2px; }

  .card--back .brand { position: absolute; left: 44px; top: 52px; gap: 10px; }
  .card--back .brand__mark { width: 34px; height: 34px; background: var(--teal); }
  .card--back .brand__name { color: var(--navy); font-size: 31px; }
  .card--back .tagline {
    position: absolute; left: 88px; top: 92px; color: var(--teal); font-size: 9px;
  }

  .contacts {
    position: absolute; left: 44px; bottom: 44px; list-style: none;
    display: flex; flex-direction: column; gap: 10px;
  }
  .contacts li { display: flex; align-items: center; gap: 12px; color: var(--ink); font-size: 17px; }
  .contacts__icon {
    width: 26px; height: 26px; background: var(--teal);
    display: flex; align-items: center; justify-content: center;
  }
  .address {
    position: absolute; right: 40px; bottom: 80px; width: 250px;
    text-align: center; color: var(--white); font-size: 16px; line-height: 1.35;
  }
  .address svg { display: block; margin: 0 auto 8px; }
</style>
</head>
<body>

<section class="card card--front">
  <div class="brand">
    <span class="brand__mark"></span>
    <span class="brand__name">BRIGHTVALE INC.</span>
  </div>
  <p class="tagline">Where Shine Counts</p>
  <p class="web">www.thebrightvale.ca</p>
</section>

<section class="card card--back">
  <div class="panel"></div>
  <div class="ribbon">
    <p class="ribbon__name">MAREN HOLT</p>
    <p class="ribbon__role">Owner</p>
  </div>
  <div class="ribbon__fold"></div>

  <div class="brand">
    <span class="brand__mark"></span>
    <span class="brand__name">BRIGHTVALE INC.</span>
  </div>
  <p class="tagline">Where Shine Counts</p>

  <ul class="contacts">
    <li>
      <span class="contacts__icon">
        <svg width="16" height="16" viewBox="0 0 24 24"><path fill="#fff" d="M6.6 10.8a15.1 15.1 0 0 0 6.6 6.6l2.2-2.2c.3-.3.7-.4 1-.2 1.1.4 2.3.6 3.6.6.6 0 1 .4 1 1V20c0 .6-.4 1-1 1A17 17 0 0 1 3 4c0-.6.4-1 1-1h3.5c.6 0 1 .4 1 1 0 1.3.2 2.5.6 3.6.1.3 0 .7-.2 1z"/></svg>
      </span>555-014-2288
    </li>
    <li>
      <span class="contacts__icon">
        <svg width="16" height="16" viewBox="0 0 24 24" fill="none" stroke="#fff" stroke-width="2"><rect x="3" y="5" width="18" height="14"/><path d="M3 5l9 8 9-8"/></svg>
      </span>hello@thebrightvale.ca
    </li>
    <li>
      <span class="contacts__icon">
        <svg width="16" height="16" viewBox="0 0 24 24" fill="none" stroke="#fff" stroke-width="2"><circle cx="12" cy="12" r="9"/><path d="M3 12h18M12 3c3 3 3 15 0 18M12 3c-3 3-3 15 0 18"/></svg>
      </span>www.thebrightvale.ca
    </li>
  </ul>

  <p class="address">
    <svg width="16" height="20" viewBox="0 0 24 30"><path fill="#fff" d="M12 0a11 11 0 0 0-11 11c0 8 11 19 11 19s11-11 11-19A11 11 0 0 0 12 0zm0 15a4 4 0 1 1 0-8 4 4 0 0 1 0 8z"/></svg>
    48 Harbour Lane, Linden Park<br>Suite 12, Elm Road
  </p>
</section>

</body>
</html>
```